Stationary and email footer design using existing Logo design

Using the Logo design I currently have I need now to have this applied to all stationary requirements including email footer, Letter Head and footer, envelopes both window and non window ( standard letter size ).
You previously did the Logo and business cards so that's good.

```html
<!DOCTYPE html>
<html lang="en">
<head>
<meta charset="utf-8">
<title>Violet Crane Stationery</title>
<link rel="stylesheet" href="https://fonts.googleapis.com/css2?family=Lato:wght@400;700&display=swap">
<style>
  :root {
    --bg: #d9d9d9;
    --paper: #ffffff;
    --lilac: #c6a8d1;
    --lilac-text: #b595c4;
    --stone: #bfbab3;
    --ink: #555555;
    --ink-dark: #333333;
  }
  * { box-sizing: border-box; margin: 0; padding: 0; }
  html, body { width: 1200px; height: 1200px; overflow: hidden; }
  body {
    background: var(--bg);
    font-family: 'Lato', sans-serif;
    color: var(--ink);
    position: relative;
  }
  .sheet {
    position: absolute;
    background: var(--paper);
    overflow: hidden;
    box-shadow: 0 6px 10px rgba(0,0,0,0.12);
  }
  .wave { position: absolute; left: 0; bottom: 0; width: 100%; height: 100%; }
  .brand { position: absolute; text-align: center; color: var(--lilac-text); }
  .brand-mark { width: 14px; height: 14px; background: var(--lilac); margin: 0 auto 6px; }
  .brand-name { font-weight: 400; letter-spacing: 0.08em; line-height: 1; text-transform: uppercase; }
  .brand-tag { letter-spacing: 0.12em; text-transform: uppercase; margin-top: 2px; line-height: 1; }
  .contact { position: absolute; list-style: none; }
  .contact li { display: flex; align-items: flex-start; }
  .contact svg { flex: none; fill: var(--lilac-text); }

  /* Letterhead */
  .letterhead { left: 79px; top: 194px; width: 469px; height: 664px; }
  .letterhead .brand { left: 31px; top: 50px; width: 110px; }
  .letterhead .brand-name { font-size: 15px; }
  .letterhead .brand-tag { font-size: 5.5px; }
  .letter-meta { position: absolute; left: 29px; right: 29px; top: 202px; display: flex; justify-content: space-between; font-size: 7.5px; }
  .letter-body { position: absolute; left: 29px; width: 411px; top: 232px; font-size: 7.4px; line-height: 12.6px; text-align: justify; }
  .letter-body p { margin-bottom: 12px; }
  .signature { position: absolute; left: 29px; top: 374px; width: 90px; height: 31px; background: linear-gradient(90deg, #e7e8f3, #f6f6fb); }
  .signer { position: absolute; left: 29px; top: 410px; }
  .signer-name { font-size: 11px; color: var(--ink-dark); }
  .signer-role { font-size: 7.5px; margin-top: 1px; }
  .letterhead .contact { left: 29px; top: 520px; font-size: 7.5px; line-height: 13px; }
  .letterhead .contact svg { width: 8px; height: 8px; margin: 2px 9px 0 0; }
  .letterhead .contact .indent { padding-left: 17px; }

  /* Envelopes */
  .envelope { left: 622px; width: 511px; height: 255px; }
  .envelope-window { top: 194px; }
  .envelope-plain { top: 488px; border-top: 5px solid var(--lilac); }
  .envelope .brand { left: 44px; top: 52px; width: 92px; }
  .envelope .brand-name { font-size: 13px; }
  .envelope .brand-tag { font-size: 5px; }
  .envelope .contact { left: 43px; top: 151px; font-size: 9.2px; line-height: 14px; }
  .envelope .contact svg { width: 9px; height: 9px; margin: 2px 9px 0 0; }
  .envelope .contact .indent { padding-left: 18px; }
  .address-window { position: absolute; left: 286px; top: 129px; width: 187px; height: 88px; border-radius: 14px; background: linear-gradient(100deg, #f4f4f4, #ffffff 55%, #f3f3f3); border: 1px solid #dcdcdc; }
  .envelope-back { top: 793px; left: 622px; width: 511px; height: 255px; }
  .back-flap { position: absolute; left: 0; top: 0; width: 511px; height: 84px; }
  .back-flap .brand { left: 0; right: 0; top: 28px; color: var(--paper); }
  .back-flap .brand-name { font-size: 16px; }

  /* Email footer */
  .email-footer { left: 80px; top: 907px; width: 468px; height: 141px; }
  .portrait { position: absolute; left: 50px; top: 19px; width: 55px; height: 55px; background: linear-gradient(160deg, #9fb0c4, #5d6d80 70%, #2c3340); }
  .footer-person { position: absolute; left: 49px; top: 84px; color: var(--lilac-text); text-transform: uppercase; }
  .footer-person .name { font-size: 12px; letter-spacing: 0.06em; line-height: 1; }
  .footer-person .role { font-size: 7.5px; letter-spacing: 0.06em; margin-top: 2px; }
  .email-footer .contact { left: 161px; top: 26px; font-size: 7.6px; line-height: 12.5px; }
  .email-footer .contact svg { width: 8px; height: 8px; margin: 2px 10px 0 0; }
  .email-footer .contact .indent { padding-left: 18px; }
  .social-row { position: absolute; left: 179px; top: 89px; display: flex; gap: 5px; }
  .social-row span { width: 14px; height: 14px; background: var(--lilac); }
  .email-footer .brand { left: 340px; top: 27px; width: 80px; }
  .email-footer .brand-name { font-size: 11px; }
  .email-footer .brand-tag { font-size: 4.5px; }
</style>
</head>
<body>
<svg width="0" height="0" style="position:absolute">
  <symbol id="icon-phone" viewBox="0 0 16 16"><path d="M3 1l3 3-2 2c1 2 3 4 6 6l2-2 3 3-2 2C7 14 2 9 1 3z"/></symbol>
  <symbol id="icon-pin" viewBox="0 0 16 16"><path d="M8 0a5.5 5.5 0 0 0-5.5 5.5C2.5 10 8 16 8 16s5.5-6 5.5-10.5A5.5 5.5 0 0 0 8 0zm0 8a2.5 2.5 0 1 1 0-5 2.5 2.5 0 0 1 0 5z"/></symbol>
  <symbol id="icon-mail" viewBox="0 0 16 16"><path d="M1 3h14v10H1zm1.5 1.5L8 9l5.5-4.5z"/></symbol>
</svg>

<!-- Letterhead -->
<section class="sheet letterhead">
  <div class="brand">
    <div class="brand-mark"></div>
    <div class="brand-name">Violet Crane</div>
    <div class="brand-tag">Wealth Planners</div>
  </div>
  <div class="letter-meta"><span>Dear, Mr____________</span><span>Date : 02.07.2019</span></div>
  <div class="letter-body">
    <p>Lorem Ipsum is simply dummy text of the printing and typesetting industry. Lorem Ipsum has been the industry's standard dummy text ever since the1500s,when an unknown printer took a galley of type and scrambled it to make a type specimen book. It has survived not only five centuries, but also the leap into electronic typesetting, remaining essentially unchanged.</p>
    <p>Lorem Ipsum is simply dummy text of the printing and typesetting industry. Lorem Ipsum has been the industry's standard dummy text ever since the1500s.</p>
    <p>Lorem Ipsum is simply dummy text of the printing and typesetting industry.</p>
  </div>
  <div class="signature" role="img" aria-label="Handwritten signature"></div>
  <div class="signer">
    <div class="signer-name">Daniel Moore</div>
    <div class="signer-role">Designation</div>
  </div>
  <ul class="contact">
    <li><svg><use href="#icon-phone"/></svg>08 5550 1234</li>
    <li><svg><use href="#icon-pin"/></svg>Suite 4, Level 2 Harbour Point</li>
    <li class="indent">12 Example Street Westfield WA 6000</li>
    <li><svg><use href="#icon-mail"/></svg>daniel.moore@vcwealth.com.au</li>
  </ul>
  <svg class="wave" viewBox="0 0 756 1070" preserveAspectRatio="none">
    <path d="M0 1038 C320 1030 660 960 756 835 L756 1070 L0 1070 Z" fill="var(--lilac)"/>
    <path d="M0 1049 C330 1046 660 1000 756 905 L756 1070 L0 1070 Z" fill="var(--paper)"/>
    <path d="M0 1054 C340 1052 670 1008 756 917 L756 1070 L0 1070 Z" fill="var(--stone)"/>
  </svg>
</section>

<!-- Window envelope -->
<section class="sheet envelope envelope-window">
  <svg class="wave" viewBox="0 0 823 411" preserveAspectRatio="none">
    <path d="M0 380 C340 370 700 300 823 155 L823 411 L0 411 Z" fill="var(--lilac)"/>
    <path d="M0 389 C350 385 710 335 823 235 L823 411 L0 411 Z" fill="var(--paper)"/>
    <path d="M0 393 C360 390 715 345 823 245 L823 411 L0 411 Z" fill="var(--stone)"/>
  </svg>
  <div class="brand">
    <div class="brand-mark"></div>
    <div class="brand-name">Violet Crane</div>
    <div class="brand-tag">Wealth Planners</div>
  </div>
  <ul class="contact">
    <li><svg><use href="#icon-phone"/></svg>08 5550 1234</li>
    <li><svg><use href="#icon-pin"/></svg>Suite 4, Level 2 Harbour Point</li>
    <li class="indent">12 Example Street Westfield WA 6000</li>
    <li><svg><use href="#icon-mail"/></svg>daniel.moore@vcwealth.com.au</li>
  </ul>
  <div class="address-window"></div>
</section>

<!-- Standard envelope -->
<section class="sheet envelope envelope-plain">
  <svg class="wave" viewBox="0 0 823 411" preserveAspectRatio="none">
    <path d="M0 380 C340 370 700 300 823 155 L823 411 L0 411 Z" fill="var(--lilac)"/>
    <path d="M0 389 C350 385 710 335 823 235 L823 411 L0 411 Z" fill="var(--paper)"/>
    <path d="M0 393 C360 390 715 345 823 245 L823 411 L0 411 Z" fill="var(--stone)"/>
  </svg>
  <div class="brand">
    <div class="brand-mark"></div>
    <div class="brand-name">Violet Crane</div>
    <div class="brand-tag">Wealth Planners</div>
  </div>
  <ul class="contact">
    <li><svg><use href="#icon-phone"/></svg>08 5550 1234</li>
    <li><svg><use href="#icon-pin"/></svg>Suite 4, Level 2 Harbour Point</li>
    <li class="indent">12 Example Street Westfield WA 6000</li>
    <li><svg><use href="#icon-mail"/></svg>daniel.moore@vcwealth.com.au</li>
  </ul>
</section>

<!-- Envelope back -->
<section class="sheet envelope-back">
  <svg class="back-flap" viewBox="0 0 511 84" preserveAspectRatio="none">
    <path d="M0 0 H511 L500 70 Q498 84 484 84 H27 Q13 84 11 70 Z" fill="var(--lilac)"/>
  </svg>
  <div class="back-flap" style="pointer-events:none">
    <div class="brand">
      <div class="brand-name">Violet Crane</div>
    </div>
  </div>
</section>

<!-- Email footer -->
<section class="sheet email-footer">
  <svg class="wave" viewBox="0 0 754 227" preserveAspectRatio="none">
    <path d="M0 212 C330 205 650 160 754 92 L754 227 L0 227 Z" fill="var(--lilac)"/>
    <path d="M0 217 C340 214 660 180 754 135 L754 227 L0 227 Z" fill="var(--paper)"/>
    <path d="M0 220 C350 218 665 186 754 142 L754 227 L0 227 Z" fill="var(--stone)"/>
  </svg>
  <div class="portrait" role="img" aria-label="Portrait photo of Daniel Moore"></div>
  <div class="footer-person">
    <div class="name">Daniel Moore</div>
    <div class="role">Designation</div>
  </div>
  <ul class="contact">
    <li><svg><use href="#icon-phone"/></svg>08 5550 1234</li>
    <li><svg><use href="#icon-pin"/></svg>Suite 4, Level 2 Harbour Point</li>
    <li class="indent">12 Example Street Westfield WA 6000</li>
    <li><svg><use href="#icon-mail"/></svg>daniel.moore@vcwealth.com.au</li>
  </ul>
  <div class="social-row" aria-label="Social links">
    <span></span><span></span><span></span><span></span><span></span>
  </div>
  <div class="brand">
    <div class="brand-mark"></div>
    <div class="brand-name">Violet Crane</div>
    <div class="brand-tag">Wealth Planners</div>
  </div>
</section>
</body>
</html>
```